Corrigan Architecture (business card)

We need a business card design. We are a full service architectural firm that specializes in mostly residential projects and some commercial projects. We are located in Hudson Valley, New York. We work with high end clients and want a business card that is memorable and has a sleek, modern, design but will not go out of style (timeless).

Target Market(s)

high end residential clients

Industry/Entity Type

Architect

Contact Information for Business Card

Front of card
Company Logo
website: www.corriganarchitectur.example
what we do: residential, Commercial

back of card
Owner's Name: Dorian Corrigan
owner's title: Principal
Business address: 2873 Route 92 Suite A, Brellfordton, NY 12688
phone number: 845-608-2917
e-mail: dc@corriganarchitecture.example

We like:
icons
sleek and clean design
simple not too busy or too much text

Font styles to use
Sans Serif

Colors
0356a4

Requirements
Must have
• company colors are navy blue, white, and gray
• Front of card
• Company Logo
• website: www.corriganarchitectur.example
• what we do: residential, Commercial
• back of card
• Owner's Name: Dorian Corrigan
• owner's title: Principal
• Business address: 2873 Route 92 Suite A, Brellfordton, NY 12688
• phone number: 845-608-2917
• e-mail: dc@corriganarchitecture.example
Nice to have
• We like:
• icons
• sleek and clean design
• simple not too much text
• color of the card to be either blue or gray
Should not have
• we do not like houses in the design or plans of houses-this is over done and we don't like it.
• no QR CODES

```html
<!DOCTYPE html>
<html lang="en">
<head>
<meta charset="utf-8">
<title>Corrigan Architecture – Business Card</title>
<link href="https://fonts.googleapis.com/css2?family=Roboto:wght@400;500;700&display=swap" rel="stylesheet">
<style>
  :root {
    --navy: #2c2a6e;
    --gray: #8a8a8c;
    --text-gray: #555558;
    --white: #ffffff;
    --stage: #e6e6e8;
  }
  * { margin: 0; padding: 0; box-sizing: border-box; }
  html, body { width: 1200px; height: 800px; overflow: hidden; }
  body {
    background: var(--stage);
    font-family: 'Roboto', Arial, sans-serif;
    position: relative;
  }
  .card {
    position: absolute;
    width: 600px;
    height: 343px;
    overflow: hidden;
    box-shadow: 0 6px 18px rgba(0,0,0,0.18);
  }

  /* Front */
  .card-front { left: 130px; top: 40px; background: var(--navy); color: var(--white); }
  .front-brand {
    position: absolute; left: 0; right: 0; top: 120px;
    display: flex; align-items: center; justify-content: center; gap: 16px;
  }
  .brand-square { width: 34px; height: 34px; border: 3px solid var(--white); flex: none; }
  .brand-name {
    font-size: 30px; font-weight: 400; letter-spacing: 2px; text-transform: uppercase; line-height: 1;
    white-space: nowrap;
  }
  .brand-name small { font-size: 14px; letter-spacing: 1px; }
  .services {
    position: absolute; left: 0; right: 0; top: 232px;
    display: flex; justify-content: center; gap: 18px;
    font-size: 16px; letter-spacing: 0.5px;
  }
  .services li { list-style: none; display: flex; align-items: center; gap: 5px; }
  .services li::before {
    content: ""; width: 8px; height: 8px; border-radius: 50%; background: var(--white);
  }

  /* Back */
  .card-back { left: 470px; top: 410px; background: var(--white); }
  .bands { position: absolute; left: 0; top: 0; width: 600px; height: 343px; }
  .side-tab {
    position: absolute; left: 0; top: 58px; width: 14px; height: 40px;
    background: var(--navy); border-radius: 0 6px 6px 0;
  }
  .owner { position: absolute; left: 40px; top: 50px; }
  .owner-name { color: var(--navy); font-size: 24px; font-weight: 700; letter-spacing: 0.5px; }
  .owner-title { color: var(--text-gray); font-size: 19px; font-weight: 700; margin-top: 2px; }
  .address {
    position: absolute; left: 40px; top: 166px;
    color: var(--text-gray); font-size: 17px; line-height: 1.25; font-style: normal;
  }
  .contacts { position: absolute; left: 40px; top: 220px; list-style: none; }
  .contacts li {
    display: flex; align-items: center; gap: 8px;
    color: var(--text-gray); font-size: 17px; line-height: 1.4;
  }
  .contacts svg { width: 15px; height: 15px; fill: var(--navy); flex: none; }
  .contacts strong { color: var(--navy); font-weight: 700; }
  .back-brand {
    position: absolute; right: 30px; top: 150px;
    display: flex; align-items: center; gap: 10px;
    color: var(--navy);
  }
  .back-brand .brand-square { width: 24px; height: 24px; border: 3px solid var(--navy); }
  .back-brand .brand-name { font-size: 19px; letter-spacing: 1.5px; }
  .back-brand .brand-name small { font-size: 10px; }
</style>
</head>
<body>

<section class="card card-front" aria-label="Card front">
  <div class="front-brand">
    <span class="brand-square"></span>
    <span class="brand-name">Corrigan Architecture <small>PLLC</small></span>
  </div>
  <ul class="services">
    <li>Residential</li>
    <li>Commercial</li>
  </ul>
</section>

<section class="card card-back" aria-label="Card back">
  <svg class="bands" viewBox="0 0 600 343" aria-hidden="true">
    <polygon points="0,327 425,316 425,343 0,343" fill="var(--navy)"/>
    <polygon points="425,316 600,311 600,343 425,343" fill="var(--gray)"/>
  </svg>
  <span class="side-tab"></span>
  <div class="owner">
    <h1 class="owner-name">DORIAN CORRIGAN</h1>
    <p class="owner-title">Principal</p>
  </div>
  <address class="address">
    2873 Route 92 Suite A,<br>Brellfordton, NY 12688
  </address>
  <ul class="contacts">
    <li>
      <svg viewBox="0 0 24 24"><path d="M6.6 10.8a15.1 15.1 0 0 0 6.6 6.6l2.2-2.2a1 1 0 0 1 1-.25 11.4 11.4 0 0 0 3.6.57 1 1 0 0 1 1 1V20a1 1 0 0 1-1 1A17 17 0 0 1 3 4a1 1 0 0 1 1-1h3.5a1 1 0 0 1 1 1c0 1.25.2 2.45.57 3.57a1 1 0 0 1-.25 1z"/></svg>
      845-608-2917
    </li>
    <li>
      <svg viewBox="0 0 24 24"><path d="M2 5h20v14H2zm2 2v.5l8 5 8-5V7l-8 5z"/></svg>
      dc@corriganarchitecture.example
    </li>
    <li>
      <svg viewBox="0 0 24 24"><path d="M12 2a10 10 0 1 0 0 20 10 10 0 0 0 0-20zm6.9 6h-3a15 15 0 0 0-1.3-4 8 8 0 0 1 4.3 4zM12 4c.8 1.2 1.5 2.5 1.9 4h-3.8c.4-1.5 1.1-2.8 1.9-4zM4.3 14a8 8 0 0 1 0-4h3.4a16 16 0 0 0 0 4zm.8 2h3a15 15 0 0 0 1.3 4 8 8 0 0 1-4.3-4zm3-8h-3a8 8 0 0 1 4.3-4 15 15 0 0 0-1.3 4zM12 20c-.8-1.2-1.5-2.5-1.9-4h3.8c-.4 1.5-1.1 2.8-1.9 4zm2.3-6H9.7a14 14 0 0 1 0-4h4.6a14 14 0 0 1 0 4zm.3 5.6a15 15 0 0 0 1.3-3.6h3a8 8 0 0 1-4.3 3.6zm1.7-5.6a16 16 0 0 0 0-4h3.4a8 8 0 0 1 0 4z"/></svg>
      <span>www.<strong>corriganarchitecture</strong>.example</span>
    </li>
  </ul>
  <div class="back-brand">
    <span class="brand-square"></span>
    <span class="brand-name">Corrigan Architecture <small>PLLC</small></span>
  </div>
</section>

</body>
</html>
```